Kovix Tralo Mart Listing Screenshot Design

We would like to create new screenshots for our Kovix app in the Tralo Mart to A/B test against the current version.

You can view our current Kovix Tralo Mart listing here: https://apps.tralomart.example/listing?id=com.quorvantic.kovix&hl=en

Attached I have added screenshots of the app that I would like to be included. Please edit the screenshots to generic text (e.g. John Smith, 123 Main St, etc.).

You can use the same text we have in the current ones. For text for the criminal screenshot please view our Zyn Zeph Shop listing: https://apps.zephshop.example/us/app/quorvantic-background-check/id907164352?mt=8

If you want to come up with new text please feel free to!

I also attached a few examples of other app screenshots that we like.

Kovix TraloMart Listing Guidelines: https://help.tralomart.example/tralomart/kovix-developer/answer/5526193?hl=en

Industry/Entity Type

Store

Font styles to use
Sans Serif

Colors
f0f0f0

Requirements
Must have
• ~Generic names and data like "John Smith", "54 Main St. Springfield, NJ 09876"
• ~Screenshot for Person Search, Criminal Records, Phone Search, Email Search, and Property Search. In that order.
• ~Headlines either the ones used in our current screenshots (https://apps.tralomart.example/listing?id=com.quorvantic.kovix&hl=en) or new ones you come up with.
• ~Must meet Kovix screenshot guidelines.
• ~Optimized for downloads.
• Must use following color palette:
• Dark purple #3B2469
• Light purple #7E6F9C
• Very dark gray #333333
• Dark gray #666666
• Gray #999999
• Blue gray #CFD9DE
• Green #5CB85C
• Navy #003577
• Yellow #F3B607
• Magenta #F0386B

```html
<!DOCTYPE html>
<html lang="en">
<head>
<meta charset="utf-8">
<title>Check Criminal Records</title>
<link href="https://fonts.googleapis.com/css2?family=Roboto:wght@400;500&display=swap" rel="stylesheet">
<style>
  :root {
    --bg-light: #999999;
    --bg-mid: #6f6f6f;
    --bg-dark: #333333;
    --badge: #cfd9de;
    --device: #1c1c1c;
    --device-edge: #3a3a3a;
    --status-bar: #3b2469;
    --app-bar: #4a2f80;
    --tab-bar: #7e6f9c;
    --white: #ffffff;
    --label: #999999;
    --value: #333333;
  }
  * { margin: 0; padding: 0; box-sizing: border-box; }
  html, body { width: 675px; height: 1200px; overflow: hidden; }
  body { position: relative; font-family: 'Roboto', sans-serif; background: var(--bg-light); }
  .backdrop { position: absolute; inset: 0; }
  .badge {
    position: absolute; left: 77px; top: 51px; width: 122px; height: 122px;
    border-radius: 50%; background: var(--badge);
  }
  .badge svg { position: absolute; left: 15px; top: 20px; }
  .headline {
    position: absolute; left: 221px; top: 52px; color: var(--white);
    font-size: 57px; font-weight: 500; line-height: 59px; letter-spacing: 0.5px;
  }
  .device {
    position: absolute; left: 66px; top: 283px; width: 542px; height: 1000px;
    background: var(--device); border: 3px solid var(--device-edge); border-radius: 62px;
  }
  .camera { position: absolute; left: 159px; top: 318px; width: 16px; height: 16px; border-radius: 50%; background: #2c2c2c; }
  .speaker { position: absolute; left: 237px; top: 319px; width: 197px; height: 17px; border-radius: 9px; background: #2a2a2a; }
  .screen { position: absolute; left: 90px; top: 391px; width: 493px; height: 820px; background: var(--white); overflow: hidden; }
  .status-bar { height: 34px; background: var(--status-bar); color: var(--white); position: relative; font-size: 20px; }
  .status-bar .time { position: absolute; right: 15px; top: 5px; font-size: 22px; }
  .status-bar .battery-pct { position: absolute; right: 115px; top: 8px; font-size: 15px; }
  .status-bar svg { position: absolute; top: 8px; }
  .app-bar { height: 76px; background: var(--app-bar); position: relative; color: var(--white); }
  .app-bar .person-name { position: absolute; left: 104px; top: 24px; font-size: 25px; font-weight: 500; }
  .app-bar svg { position: absolute; }
  .tab-bar { height: 65px; background: var(--tab-bar); position: relative; font-size: 17.5px; font-weight: 500; white-space: nowrap; }
  .tab-bar .tab { position: absolute; top: 24px; color: rgba(255,255,255,0.55); }
  .tab-bar .tab.active { color: var(--white); left: 109px; }
  .tab-bar .indicator { position: absolute; left: 94px; bottom: 0; width: 306px; height: 3px; background: var(--white); }
  .record { padding-left: 7px; }
  .record dt { color: var(--label); font-size: 19.5px; font-weight: 500; margin-top: 7px; height: 29px; line-height: 29px; }
  .record dd { color: var(--value); font-size: 21px; height: 45px; line-height: 41px; }
</style>
</head>
<body>
  <svg class="backdrop" width="675" height="1200" viewBox="0 0 675 1200" aria-hidden="true">
    <polygon points="0,380 675,560 675,1200 0,1200" fill="var(--bg-mid)"/>
    <polygon points="675,865 675,1200 0,1200 0,1027" fill="var(--bg-dark)"/>
  </svg>

  <div class="badge">
    <svg width="92" height="82" viewBox="0 0 92 82" aria-hidden="true">
      <circle cx="20" cy="48" r="16" fill="none" stroke="#000" stroke-width="6"/>
      <circle cx="64" cy="52" r="16" fill="none" stroke="#000" stroke-width="6"/>
      <path d="M28 32 q10 -18 22 -12 q10 6 8 18" fill="none" stroke="#000" stroke-width="4" stroke-dasharray="5 3"/>
      <rect x="22" y="26" width="12" height="10" fill="#000"/>
      <rect x="54" y="30" width="12" height="10" fill="#000"/>
    </svg>
  </div>
  <h1 class="headline">Check Criminal<br>Records</h1>

  <div class="device"></div>
  <div class="camera"></div>
  <div class="speaker"></div>

  <main class="screen">
    <div class="status-bar">
      <svg style="left:14px" width="18" height="18" viewBox="0 0 18 18"><rect x="1" y="1" width="16" height="16" fill="none" stroke="#fff" stroke-width="2"/><path d="M3 14 l4 -5 3 3 2 -2 3 4z" fill="#fff"/></svg>
      <svg style="left:49px" width="20" height="18" viewBox="0 0 20 18"><rect x="1" y="2" width="18" height="14" fill="none" stroke="#fff" stroke-width="2"/><path d="M2 3 l8 7 8 -7" fill="none" stroke="#fff" stroke-width="2"/></svg>
      <svg style="left:87px" width="16" height="18" viewBox="0 0 16 18"><rect x="1" y="1" width="14" height="16" fill="#fff"/><path d="M5 7 l6 6 M11 7 l-6 6" stroke="#d33" stroke-width="2"/></svg>
      <svg style="left:265px" width="22" height="18" viewBox="0 0 22 18"><path d="M2 6 h4 l5 -4 v14 l-5 -4 h-4z" fill="#fff"/><path d="M14 2 l7 14" stroke="#fff" stroke-width="2"/></svg>
      <svg style="left:297px" width="24" height="20" viewBox="0 0 24 20"><path d="M2 7 a14 14 0 0 1 20 0 M5 10 a9 9 0 0 1 14 0 M8 13 a5 5 0 0 1 8 0" fill="none" stroke="#fff" stroke-width="2"/><circle cx="12" cy="17" r="2" fill="#fff"/></svg>
      <svg style="left:334px" width="22" height="20" viewBox="0 0 22 20"><path d="M21 1 v18 h-20z" fill="rgba(255,255,255,0.6)"/></svg>
      <span class="battery-pct">18%</span>
      <svg style="left:392px" width="12" height="20" viewBox="0 0 12 20"><rect x="1" y="2" width="10" height="17" fill="none" stroke="#fff" stroke-width="1.5"/><rect x="4" y="0" width="4" height="2" fill="#fff"/><rect x="2" y="15" width="8" height="3" fill="#fff"/></svg>
      <span class="time">5:08 PM</span>
    </div>

    <header class="app-bar">
      <svg style="left:27px;top:26px" width="26" height="24" viewBox="0 0 26 24"><path d="M24 12 H4 M12 3 L3 12 L12 21" fill="none" stroke="#fff" stroke-width="3"/></svg>
      <span class="person-name">JOHN DOE</span>
      <svg style="left:329px;top:21px" width="32" height="34" viewBox="0 0 32 34"><path d="M16 3 c-7 0 -10 5 -10 11 v7 l-4 5 h28 l-4 -5 v-7 c0 -6 -3 -11 -10 -11z" fill="#fff"/><circle cx="16" cy="30" r="3.5" fill="#fff"/><path d="M10 16 l4 4 8 -8" fill="none" stroke="var(--app-bar)" stroke-width="3"/></svg>
      <svg style="left:397px;top:23px" width="30" height="30" viewBox="0 0 30 30"><circle cx="15" cy="15" r="13" fill="none" stroke="#fff" stroke-width="2.5"/><path d="M11 12 a4 4 0 1 1 5 4 v3" fill="none" stroke="#fff" stroke-width="2.5"/><circle cx="16" cy="23" r="1.6" fill="#fff"/></svg>
      <svg style="left:456px;top:25px" width="8" height="26" viewBox="0 0 8 26"><circle cx="4" cy="4" r="3" fill="#fff"/><circle cx="4" cy="13" r="3" fill="#fff"/><circle cx="4" cy="22" r="3" fill="#fff"/></svg>
    </header>

    <nav class="tab-bar">
      <span class="tab" style="left:2px">GHBORS</span>
      <span class="tab active">CRIMINAL &amp; TRAFFIC RECORDS</span>
      <span class="tab" style="left:417px">BANKRU</span>
      <span class="indicator"></span>
    </nav>

    <dl class="record">
      <dt>OFFENSE DATE</dt><dd>Feb 24, 2009</dd>
      <dt>DESCRIPTION OF OFFENSE</dt><dd>AGGRAVATED ASSAULT, ATTEMPT TO COMMIT</dd>
      <dt>OFFENSE TYPE</dt><dd>Department Of Correction</dd>
      <dt>CASE NUMBER</dt><dd>N/A</dd>
      <dt>AGENCY</dt><dd>N/A</dd>
      <dt>DATE</dt><dd>N/A</dd>
      <dt>OFFENSE DETAILS</dt><dd>AGGRAVATED ASSAULT, ATTEMPT TO COMMIT</dd>
      <dt>DISPOSITION</dt><dd>N/A</dd>
    </dl>
  </main>
</body>
</html>
```